public page walrus GX (www.walrusgx.com)

https://www.quillbarn.net/shard/s412/sh/a3b1c9d2-58e4-4f7a-b2c6-1d9e0f7a3b45/41c7e2a9d08b6f53e17a92c4d6b0f831

compatible with wordpress

Designs look the same

Industry/Entity Type

Finance And Accounting

Coding

Coded - Design and coding required

Number of Pages Required

1 page

Font styles to use
Sans Serif

Colors
85cae6
3176b5
cfdeed
fac994
fff3d1
fefdec
cfcfcf
e8e8e8
9d9d9d

```html
<!DOCTYPE html>
<html lang="en">
<head>
<meta charset="utf-8">
<title>walrus GX – Real Result, Accurate Works</title>
<link href="https://fonts.googleapis.com/css2?family=Poppins:wght@300;400;500;600;700&display=swap" rel="stylesheet">
<style>
:root{
  --blue:#3176b5;
  --blue-deep:#1f5fa8;
  --sky:#85cae6;
  --ice:#cfdeed;
  --orange:#f5a23a;
  --peach:#fac994;
  --cream:#fff3d1;
  --ivory:#fefdec;
  --grey-1:#cfcfcf;
  --grey-2:#e8e8e8;
  --grey-3:#9d9d9d;
  --ink:#2b2f3a;
  --text:#6e737c;
  --white:#ffffff;
}
*{box-sizing:border-box;margin:0;padding:0}
html,body{width:1200px;height:3956px;overflow:hidden;background:var(--white)}
body{font-family:"Poppins",sans-serif;color:var(--text);font-size:12px;line-height:1.6}
.page{position:relative;width:1200px;height:3956px;overflow:hidden}
.abs{position:absolute}
.btn{display:inline-block;border-radius:20px;font-weight:600;font-size:10px;letter-spacing:.5px;text-transform:uppercase;text-align:center}
.btn-orange{background:var(--orange);color:var(--white);box-shadow:0 6px 14px rgba(245,162,58,.35)}
.btn-blue{background:var(--blue);color:var(--white);box-shadow:0 6px 14px rgba(49,118,181,.35)}
.card{background:var(--white);border-radius:6px;box-shadow:0 10px 30px rgba(30,60,110,.12)}
h2.section-title{font-size:22px;color:var(--ink);font-weight:500;text-align:center;letter-spacing:.5px}

/* header */
.brand{left:28px;top:22px;display:flex;align-items:center;gap:8px}
.brand-dot{width:30px;height:30px;border-radius:50%;background:var(--blue)}
.brand-name{font-size:15px;font-weight:600;color:var(--blue)}
.nav{left:150px;top:24px;display:flex;gap:22px;font-size:9px;font-weight:600;color:var(--ink);letter-spacing:.5px}
.hero-orb{left:580px;top:-220px;width:700px;height:860px;border-radius:50%;
  background:radial-gradient(circle at 45% 60%,#4aa6ea 0%,#2f86d8 45%,#1e64bf 100%)}
.hero-dot{left:566px;top:108px;width:28px;height:28px;border-radius:50%;background:var(--orange)}
.hero-ring{left:560px;top:140px;width:70px;height:70px;border-radius:50%;border:2px solid var(--sky);opacity:.6}
.btn-signup{left:980px;top:22px;width:82px;height:26px;line-height:26px;background:var(--white);color:var(--blue)}
.btn-signin{left:1080px;top:22px;width:82px;height:26px;line-height:26px}
.hero-title{left:110px;top:228px;font-size:40px;line-height:1.05;font-weight:700;color:var(--sky);letter-spacing:1px}
.hero-title span{display:block;color:var(--grey-3);font-weight:500}
.hero-copy{left:110px;top:322px;width:360px;font-size:10px;line-height:1.6}
.hero-form{left:110px;top:380px;width:340px;height:34px;border:1px solid var(--grey-2);border-radius:20px;display:flex;align-items:center;justify-content:space-between;padding-left:18px;font-size:10px;color:var(--grey-3)}
.hero-form .btn{width:110px;height:28px;line-height:28px;margin-right:3px}

/* profit */
.orange-half{left:-320px;top:560px;width:760px;height:520px;border-radius:50%;background:var(--orange)}
.ivory-blob{left:360px;top:580px;width:320px;height:260px;border-radius:50%;background:var(--ivory)}
.chart-card{left:100px;top:690px;width:380px;height:340px;padding:22px 26px}
.chart-card .store{font-weight:700;color:var(--ink);font-size:15px}
.chart-card .label{font-size:9px;color:var(--grey-3)}
.avatar-s{width:26px;height:26px;border-radius:50%;background:linear-gradient(135deg,var(--peach),#c58b5c)}
.profit-text{left:590px;top:710px;width:440px}
.profit-text h3{font-size:22px;color:var(--ink);font-weight:500;line-height:1.35}
.profit-text .store{font-weight:700;font-size:13px;color:var(--ink);margin:14px 0 10px}
.profit-text p{font-size:10px}
.more-link{font-size:9px;font-weight:600;color:var(--blue);margin-top:18px;letter-spacing:.5px}

/* easy way */
.grey-orb{border-radius:50%;background:#f6f7f9}
.easy-text{left:210px;top:1275px;width:400px}
.easy-text h3{font-size:20px;color:var(--ink);font-weight:500;line-height:1.35;margin-bottom:16px}
.easy-text p{font-size:10px;margin-bottom:14px}
.author{display:flex;align-items:center;gap:10px;margin-top:10px}
.author b{display:block;font-size:10px;color:var(--ink)}
.author small{font-size:9px;color:var(--grey-3)}
.portrait-ring{left:700px;top:1250px;width:300px;height:300px;border-radius:50%;border:1px dashed var(--grey-1)}
.portrait{left:770px;top:1320px;width:160px;height:160px;border-radius:50%;border:6px solid var(--orange);background:linear-gradient(160deg,#f2d7b6,#c9a07a)}
.mini-face{width:30px;height:30px;border-radius:50%;background:linear-gradient(135deg,var(--grey-2),var(--grey-1))}

/* features */
.feature-card{padding:20px 18px;width:175px}
.feature-card h4{font-size:11px;color:var(--ink);font-weight:500;line-height:1.35;margin:10px 0 8px}
.feature-card p{font-size:8.5px;line-height:1.6}
.icon-box{width:36px;height:36px}
.features-text{left:600px;top:1895px;width:420px}
.features-text h3{font-size:22px;color:var(--ink);font-weight:500;margin-bottom:12px}
.features-text p{font-size:10px;margin-bottom:20px}
.features-text .btn{width:140px;height:32px;line-height:32px}

/* testimonials */
.testi{width:210px;padding:14px 16px;font-size:8.5px}
.testi .who{display:flex;gap:8px;align-items:center;margin-top:14px}
.testi .who b{display:block;color:var(--ink);font-size:9px}
.quote-badge{left:332px;top:2418px;width:30px;height:30px;border-radius:50%;background:var(--blue)}
.pager{top:2624px;width:28px;height:28px;border-radius:50%;background:var(--grey-2)}

/* faq */
.faq-item{height:24px;line-height:24px;border-radius:3px;padding-left:12px;font-size:8.5px;color:var(--white);font-weight:500;box-shadow:0 4px 10px rgba(0,0,0,.08)}
.faq-item.closed{background:var(--orange)}
.faq-item.open{background:var(--blue)}
.faq-answer{font-size:8.5px;line-height:1.6;padding:8px 12px}

/* partners */
.partner{top:3228px;height:30px;border-radius:4px;background:var(--grey-2)}

/* cta */
.cta{left:0;top:3360px;width:1200px;height:210px;background:linear-gradient(90deg,#1e7fd0,#3a9be0,#1e7fd0);text-align:center;color:var(--white)}
.cta h2{font-size:30px;font-weight:500;padding-top:42px;letter-spacing:1px}
.cta p{font-size:10px;opacity:.9;margin:6px 0 20px}
.cta .btn{width:140px;height:32px;line-height:32px}

/* footer */
.foot-col{top:3618px;width:150px}
.foot-col h5{font-size:10px;color:var(--ink);font-weight:600;margin-bottom:10px}
.foot-col li{list-style:none;font-size:8.5px;line-height:2}
.news{left:850px;top:3650px;width:240px;height:30px;border:1px solid var(--grey-2);border-radius:20px;padding-left:14px;line-height:28px;font-size:9px;color:var(--grey-3)}
.news-go{left:1060px;top:3652px;width:26px;height:26px;border-radius:50%;background:var(--orange)}
.social{top:3700px;width:16px;height:16px;border-radius:50%;background:var(--grey-2)}
.foot-bar{left:0;top:3900px;width:1200px;border-top:1px solid var(--grey-2);padding:16px 110px;font-size:8.5px;display:flex;justify-content:space-between}
</style>
</head>
<body>
<div class="page">

  <!-- header / hero -->
  <div class="abs hero-orb" role="img" aria-label="Isometric illustration of analytics dashboards and charts on a blue background"></div>
  <div class="abs hero-ring"></div>
  <div class="abs hero-dot"></div>

  <div class="abs brand"><span class="brand-dot"></span><span class="brand-name">walrus GX</span></div>
  <nav class="abs nav"><span>HOME</span><span>PRICING</span><span>ABOUT US</span><span>CONTACT</span><span>BLOG</span><span>FAQ</span></nav>
  <a class="abs btn btn-signup">Sign Up</a>
  <a class="abs btn btn-orange btn-signin">Sign In</a>

  <h1 class="abs hero-title">REAL RESULT<span>ACCURATE WORKS</span></h1>
  <p class="abs hero-copy">walrus GX helps sellers track every order, fee and margin so you can see your real profit at a glance and grow with confidence.</p>
  <div class="abs hero-form">Enter your email<span class="btn btn-orange">Get Started</span></div>

  <!-- profit section -->
  <div class="abs orange-half"></div>
  <div class="abs ivory-blob"></div>
  <div class="abs card chart-card">
    <div style="display:flex;justify-content:space-between;align-items:flex-start">
      <div><div class="store">Marketly</div><div class="label">Sales Console</div></div>
      <div class="avatar-s" role="img" aria-label="User avatar"></div>
    </div>
    <div class="label" style="margin-top:10px;color:var(--ink);font-weight:500">Make Sales</div>
    <svg width="330" height="200" viewBox="0 0 330 200" style="margin-top:6px">
      <g stroke="#e8e8e8" stroke-width="1">
        <line x1="0" y1="30" x2="330" y2="30"/><line x1="0" y1="75" x2="330" y2="75"/>
        <line x1="0" y1="120" x2="330" y2="120"/><line x1="0" y1="165" x2="330" y2="165"/>
      </g>
      <path d="M0 120 C40 100 60 70 100 78 S160 110 200 90 S260 50 300 60 L330 55 L330 170 L0 170Z" fill="#cfdeed" opacity=".5"/>
      <path d="M0 120 C40 100 60 70 100 78 S160 110 200 90 S260 50 300 60 L330 55" fill="none" stroke="#3176b5" stroke-width="2"/>
      <rect x="6" y="38" width="40" height="16" rx="3" fill="#3176b5"/>
      <text x="26" y="50" font-size="8" fill="#fff" text-anchor="middle" font-family="Poppins, sans-serif">+24 %</text>
      <rect x="270" y="20" width="44" height="16" rx="3" fill="#85cae6"/>
      <text x="292" y="32" font-size="8" fill="#fff" text-anchor="middle" font-family="Poppins, sans-serif">+36 %</text>
      <g font-size="8" fill="#9d9d9d" font-family="Poppins, sans-serif">
        <text x="10" y="190">Jan</text><text x="70" y="190">Feb</text><text x="130" y="190">Mar</text>
        <text x="190" y="190">Apr</text><text x="250" y="190">May</text><text x="305" y="190">Jun</text>
      </g>
    </svg>
    <div style="display:flex;justify-content:space-between;font-size:9px;margin-top:6px"><span>Monthly</span><span style="color:var(--blue);font-weight:600">$12,480</span></div>
  </div>
  <div class="abs profit-text">
    <h3>Are you making a Profit from<br>Marketly really Well?</h3>
    <div class="store">Marketly</div>
    <p>Most sellers never see their true numbers. Fees, refunds, ad spend and shipping quietly eat the margin on every sale. We pull all of it together in one clear view so you always know which products really pay off.</p>
    <p style="margin-top:10px">Stop guessing and start growing with reports that update themselves every day.</p>
    <div class="more-link">KNOW MORE ABOUT THE &rarr;</div>
  </div>

  <!-- easy way section -->
  <div class="abs grey-orb" style="left:-160px;top:1160px;width:520px;height:520px"></div>
  <div class="abs grey-orb" style="left:820px;top:1180px;width:520px;height:520px"></div>
  <div class="abs easy-text">
    <h3>walrus GX Provide it in a<br>Easy Way to Count</h3>
    <p>Connect your store once and we handle the rest. Every order, fee and refund is counted for you, so the profit you see is the profit you make.</p>
    <p>Simple charts, clean tables and daily alerts keep you on top of your business without spreadsheets or late nights.</p>
    <div class="author">
      <div class="avatar-s" role="img" aria-label="Customer avatar"></div>
      <div><b>Daniel Reeve</b><small>Founder, online retail brand</small></div>
    </div>
  </div>
  <div class="abs portrait-ring"></div>
  <div class="abs portrait" role="img" aria-label="Portrait photo of a smiling customer"></div>
  <div class="abs card" style="left:915px;top:1190px;width:120px;height:80px;padding:10px">
    <div style="font-size:8px;color:var(--grey-3)">Net Profit</div>
    <svg width="100" height="40" viewBox="0 0 100 40"><path d="M0 30 C20 10 35 35 55 20 S85 5 100 12" fill="none" stroke="#85cae6" stroke-width="2"/></svg>
  </div>
  <div class="abs card" style="left:700px;top:1395px;width:60px;height:32px;padding:4px 8px;font-size:9px;color:var(--blue);font-weight:600;line-height:1.3">+24 %<br><span style="font-size:7px;color:var(--grey-3);font-weight:400">Today</span></div>
  <div class="abs mini-face" style="left:744px;top:1290px" role="img" aria-label="Small user avatar"></div>
  <div class="abs mini-face" style="left:982px;top:1400px" role="img" aria-label="Small user avatar"></div>
  <div class="abs mini-face" style="left:736px;top:1540px" role="img" aria-label="Small user avatar"></div>

  <!-- features -->
  <div class="abs grey-orb" style="left:-120px;top:1740px;width:520px;height:520px"></div>
  <div class="abs card feature-card" style="left:100px;top:1780px">
    <svg class="icon-box" viewBox="0 0 36 36"><rect x="4" y="20" width="6" height="12" fill="#f5a23a"/><rect x="14" y="12" width="6" height="20" fill="#3176b5"/><rect x="24" y="6" width="6" height="26" fill="#85cae6"/></svg>
    <h4>Stats-driven Data<br>Analytics</h4>
    <p>Clear reports built from live sales data help you decide faster and spend wiser.</p>
  </div>
  <div class="abs card feature-card" style="left:100px;top:2020px">
    <svg class="icon-box" viewBox="0 0 36 36"><circle cx="18" cy="10" r="6" fill="#3176b5"/><rect x="9" y="18" width="18" height="14" rx="3" fill="#85cae6"/><rect x="4" y="32" width="28" height="2" fill="#f5a23a"/></svg>
    <h4>Expert Guidance and<br>Global Support</h4>
    <p>Our team is ready around the clock to answer questions and guide your growth.</p>
  </div>
  <div class="abs card feature-card" style="left:370px;top:1900px">
    <svg class="icon-box" viewBox="0 0 36 36"><path d="M18 3 L31 8 V18 C31 26 25 31 18 33 C11 31 5 26 5 18 V8Z" fill="#3176b5"/><path d="M12 18 l4 4 l8 -9" fill="none" stroke="#fff" stroke-width="2.5"/></svg>
    <h4>100% Security &amp; Privacy<br>Guarantee</h4>
    <p>Your data is encrypted and never shared, so you can focus on selling worry free.</p>
  </div>
  <div class="abs features-text">
    <h3>Features that Really Works</h3>
    <p>Everything you need to understand your numbers lives in one place. Track costs, compare products and plan stock with tools built for busy sellers who want answers, not more work.</p>
    <span class="btn btn-blue">Get Started Now</span>
  </div>

  <!-- testimonials -->
  <h2 class="abs section-title" style="left:0;top:2345px;width:1200px">OUR CUSTOMER TESTIMONIALS</h2>
  <div class="abs testi" style="left:140px;top:2430px;opacity:.35">
    <p>Setup took minutes and the reports are easy to read. I finally know my margins.</p>
    <div class="who"><span class="mini-face" role="img" aria-label="Customer avatar"></span><div><b>Ella Moss</b>Store owner</div></div>
  </div>
  <div class="abs card testi" style="left:350px;top:2420px;width:250px">
    <p>I used to spend hours on spreadsheets every week. Now I open one page and see exactly where my money goes. It changed how I plan every launch.</p>
    <div class="who"><span class="mini-face" role="img" aria-label="Customer avatar"></span><div><b>Liam Carter</b>Online seller</div></div>
  </div>
  <div class="quote-badge abs"><svg width="30" height="30" viewBox="0 0 30 30"><text x="15" y="23" font-size="20" fill="#fff" text-anchor="middle" font-family="Poppins, sans-serif">&ldquo;</text></svg></div>
  <div class="abs testi" style="left:630px;top:2430px">
    <p>Great support team and very clear charts. Highly recommend to any seller.</p>
    <div class="who"><span class="mini-face" role="img" aria-label="Customer avatar"></span><div><b>Nora Hale</b>Brand manager</div></div>
  </div>
  <div class="abs testi" style="left:860px;top:2430px;opacity:.6">
    <p>The daily alerts saved me from costly mistakes more than once this year.</p>
    <div class="who"><span class="mini-face" role="img" aria-label="Customer avatar"></span><div><b>Owen Price</b>Retailer</div></div>
  </div>
  <div class="abs pager" style="left:400px"></div>
  <div class="abs pager" style="left:440px;background:var(--white);border:1px solid var(--grey-2)"></div>

  <!-- faq -->
  <div class="abs grey-orb" style="left:820px;top:2720px;width:480px;height:480px"></div>
  <h2 class="abs section-title" style="left:0;top:2795px;width:1200px">FAQs</h2>
  <div class="abs" style="left:340px;top:2846px;width:250px">
    <div class="faq-item open">&#9656; How do I connect my store to walrus GX?</div>
    <div class="faq-answer">Sign in, open settings and link your seller account. Data starts to sync right away and your first report is ready within minutes.</div>
    <div class="faq-item closed" style="margin-top:6px">&#9656; How are fees and refunds counted?</div>
    <div class="faq-item closed" style="margin-top:8px">&#9656; Can I export my reports?</div>
  </div>
  <div class="abs" style="left:600px;top:2846px;width:260px">
    <div class="faq-item closed">&#9656; Is there a free trial available?</div>
    <div class="faq-item closed" style="margin-top:8px">&#9656; Which marketplaces are supported?</div>
    <div class="faq-item closed" style="margin-top:8px">&#9656; How often is my data updated?</div>
    <div class="faq-item closed" style="margin-top:8px">&#9656; Can I add team members?</div>
    <div class="faq-item closed" style="margin-top:8px">&#9656; How safe is my account data?</div>
    <div class="faq-item closed" style="margin-top:8px">&#9656; How do I cancel my plan?</div>
  </div>

  <!-- partners -->
  <h2 class="abs section-title" style="left:0;top:3170px;width:1200px">MEET OUR PARTNERS</h2>
  <div class="abs partner" style="left:0;width:70px;opacity:.5"></div>
  <div class="abs partner" style="left:140px;width:90px"></div>
  <div class="abs partner" style="left:270px;width:90px"></div>
  <div class="abs partner" style="left:400px;width:80px"></div>
  <div class="abs partner" style="left:520px;width:90px"></div>
  <div class="abs partner card" style="left:680px;top:3218px;width:140px;height:50px;background:var(--white)"></div>
  <div class="abs partner" style="left:860px;width:70px;opacity:.5"></div>

  <!-- cta -->
  <section class="abs cta">
    <h2>TRY WALRUS GX TODAY! AND GET AN EDGE</h2>
    <p>Join sellers who finally see their real profit every single day.</p>
    <span class="btn btn-orange">Get Started Now</span>
  </section>

  <!-- footer -->
  <div class="abs foot-col" style="left:110px"><h5>ABOUT US</h5><ul><li>Our Story</li><li>Careers</li><li>Blog</li><li>Press</li><li>Partners</li><li>Contact</li></ul></div>
  <div class="abs foot-col" style="left:250px"><h5>PRICING</h5><ul><li>Plans</li><li>Free Trial</li><li>Compare</li><li>Discounts</li></ul></div>
  <div class="abs foot-col" style="left:380px"><h5>KNOWLEDGE</h5><ul><li>Help Center</li><li>Guides</li><li>Webinars</li><li>Glossary</li><li>Updates</li></ul></div>
  <div class="abs foot-col" style="left:530px"><h5>ACCOUNT</h5><ul><li>Sign In</li><li>Sign Up</li><li>Settings</li></ul></div>
  <div class="abs foot-col" style="left:690px"><h5>CONTACT US</h5><ul><li>Support</li><li>Sales</li><li>Feedback</li><li>www.walrusgx.com</li></ul></div>
  <div class="abs foot-col" style="left:850px"><h5>OUR NEWSLETTER</h5></div>
  <div class="abs news">Your email</div>
  <div class="abs news-go"></div>
  <div class="abs social" style="left:870px"></div>
  <div class="abs social" style="left:894px"></div>
  <div class="abs social" style="left:918px"></div>
  <div class="abs social" style="left:942px"></div>
  <div class="abs foot-bar"><span>Copyright &copy; walrus GX. All rights reserved. &nbsp; Privacy Policy &nbsp; Terms of Use</span><span>English (US)</span></div>

</div>
</body>
</html>
```